New profile page for existing party website

For the party website 'Revelmap' we need a new design for the user profile page.

The page should show
* a profile picture
* basic information like name, age and city
* music styles he/she likes
* links to their Chatterly profile and website
* a bio (HTML content)
* events they plan to go to
* past events
* pictures

Challenge is that some users may have little information (just their name) while others have a huge description, lots of foto's, events, etc.

Please visit http://www.revelmap.example and http://www.revelmap.example/users/gordon

Target Market(s)

Men and women between 18 and 35

Industry/Entity Type

Night Club

Number of Pages Required

2 page

Font styles to use
Other font styles liked:
• Roboto

Requirements
Must have
• Please design how the page looks with a fully filled out profile and with an empty profile.
• It should fit well with the existing website.
• Include designs for both for small screens (mobile) and large screens (tablet, desktop).
Nice to have
• UX design on how to collapse or paginate sections.
• Interactive effects would be a bonus.
Should not have
• The page should not have subnavigation like menus or tabs.

```html
<!DOCTYPE html>
<html lang="nl">
<head>
<meta charset="utf-8">
<title>Revelmap – Gordon Vale</title>
<link rel="stylesheet" href="https://fonts.googleapis.com/css2?family=Roboto:wght@400;500;700&family=Roboto+Condensed:wght@300;400&display=swap">
<style>
  :root{
    --page:#252525;
    --page-dots:#2c2c2c;
    --panel:#1d1d1d;
    --rail:#0a0a0a;
    --tab:#111111;
    --bar:#000000;
    --text:#b9b9b9;
    --text-soft:#9a9a9a;
    --heading:#d2d2d2;
    --white:#ffffff;
    --badge:rgba(20,20,20,.88);
    --track:#2e2e2e;
    --thumb:#5a5a5a;
    --button:#555555;
    --frame:#050505;
  }
  *{box-sizing:border-box;margin:0;padding:0}
  html,body{width:1200px;height:2375px;overflow:hidden}
  body{
    position:relative;
    background-color:var(--page);
    background-image:radial-gradient(var(--page-dots) 1px,transparent 1px);
    background-size:4px 4px;
    font-family:"Roboto",Arial,sans-serif;
    color:var(--text);
  }

  /* top bar */
  .topbar{position:absolute;left:0;top:0;width:1200px;height:48px;background:var(--bar)}
  .brand{position:absolute;left:92px;top:9px;display:flex;align-items:center;gap:8px;
    font-family:"Roboto Condensed",sans-serif;font-size:26px;font-weight:400;color:var(--white)}
  .brand-dot{width:12px;height:12px;border-radius:50%;background:var(--white)}
  .nav{position:absolute;left:489px;top:15px;display:flex;gap:0;font-size:15px;color:#ddd}
  .nav a{color:#ddd;text-decoration:none;position:absolute;white-space:nowrap}
  .search{position:absolute;left:806px;top:11px;width:115px;height:27px;background:var(--white);
    border:0;font-size:13px;color:#999;padding:5px 9px;font-family:inherit}
  .divider{position:absolute;left:939px;top:6px;width:1px;height:36px;background:#333}
  .user-avatar{position:absolute;left:955px;top:7px;width:34px;height:34px;background:linear-gradient(135deg,#8a5a3a,#c78a5c)}
  .user-name{position:absolute;left:996px;top:15px;font-size:14px;color:#ddd}

  /* panels */
  .panel{position:absolute;left:85px;width:1030px;background:var(--panel)}
  .rail{position:absolute;left:0;bottom:0;width:39px;background:var(--rail)}
  .tab-icon{position:absolute;left:0;width:39px;height:36px;background:var(--rail);display:flex;align-items:center;justify-content:center}
  .tab-label{position:absolute;left:41px;height:36px;background:var(--tab);padding:0 24px;
    font-family:"Roboto Condensed",sans-serif;font-size:16px;color:var(--heading);line-height:36px}
  .scroll{position:absolute;left:996px;width:8px;background:var(--track);border-radius:4px}
  .scroll i{position:absolute;left:0;top:0;width:8px;background:var(--thumb);border-radius:4px}

  /* profile */
  .avatar{position:absolute;left:69px;top:92px;width:174px;height:217px;border:3px solid var(--frame);
    background:linear-gradient(160deg,#6e4a2e 0%,#a07050 45%,#d8cfc2 100%)}
  .profile-name{position:absolute;left:271px;top:88px;font-family:"Roboto Condensed",sans-serif;font-weight:300;
    font-size:33px;color:var(--heading)}
  .facts{position:absolute;left:271px;top:172px;font-size:16px;line-height:29px;color:var(--text-soft)}
  .facts b{color:var(--heading);font-weight:500}
  .manage{position:absolute;left:273px;top:279px;width:101px;height:30px;background:var(--button);
    border:1px solid #6a6a6a;font-size:12px;color:#ccc;text-align:center;line-height:28px}
  .social{position:absolute;left:908px;top:90px;display:flex;gap:10px}
  .social span{width:18px;height:18px;background:#9c9c9c;border-radius:2px}

  /* resume */
  .resume{position:absolute;left:69px;top:90px;width:900px}
  .resume h2{font-family:"Roboto Condensed",sans-serif;font-weight:400;font-size:19px;color:var(--heading);margin-bottom:12px}
  .resume p{font-size:14px;color:var(--text);margin-bottom:15px}
  .resume p.body{font-size:13px;line-height:17px;margin-bottom:20px}
  .resume h3{font-family:"Roboto Condensed",sans-serif;font-weight:400;font-size:16px;color:var(--text)}

  /* events */
  .event-img{position:absolute;left:69px;width:324px;height:130px;border:3px solid var(--frame)}
  .date{position:absolute;right:0;top:0;height:30px;padding:0 10px;background:var(--badge);
    font-family:"Roboto Condensed",sans-serif;font-size:16px;color:var(--white);line-height:30px}
  .event-info{position:absolute;left:417px;width:560px}
  .event-info h4{font-family:"Roboto Condensed",sans-serif;font-weight:400;font-size:16px;color:var(--heading);margin-bottom:8px}
  .event-info li{list-style:none;font-size:12.5px;color:var(--text);height:23px;display:flex;align-items:center;gap:12px}
  .event-info svg{flex:none}

  /* photos */
  .photo{position:absolute;border:3px solid var(--frame)}

  /* footer */
  .footer{position:absolute;left:0;top:2287px;width:1200px;height:88px;background:linear-gradient(#0b0b0b,#120606)}
  .footer-links{position:absolute;top:28px;width:100%;text-align:center;font-size:12px;font-weight:700;color:var(--white);letter-spacing:.2px}
  .footer-links span{margin:0 7px}
  .copyright{position:absolute;top:58px;width:100%;text-align:center;font-size:9px;color:#ddd}
</style>
</head>
<body>

<header class="topbar">
  <div class="brand"><span class="brand-dot"></span>Revelmap</div>
  <nav class="nav">
    <a style="left:0">Home</a>
    <a style="left:54px">Agenda</a>
    <a style="left:117px">Vrijkaarten</a>
    <a style="left:201px">Foto's</a>
    <a style="left:255px">Nieuws</a>
  </nav>
  <input class="search" value="Zoeken">
  <div class="divider"></div>
  <div class="user-avatar" role="img" aria-label="Small profile photo of Gordon Vale"></div>
  <div class="user-name">Gordon Vale ▾</div>
</header>

<!-- profile -->
<section class="panel" style="top:82px;height:387px">
  <div class="rail" style="top:34px"></div>
  <div class="tab-icon" style="top:34px">
    <svg width="16" height="16" viewBox="0 0 16 16"><circle cx="8" cy="5" r="3.5" fill="#aaa"/><path d="M1 16c0-4 3-6.5 7-6.5s7 2.5 7 6.5z" fill="#aaa"/></svg>
  </div>
  <div class="tab-label" style="top:34px">My Profile</div>
  <div class="avatar" role="img" aria-label="Profile photo of Gordon Vale"></div>
  <h1 class="profile-name">Gordon Vale</h1>
  <div class="facts">
    <div><b>Age</b> - 34</div>
    <div><b>City</b> - Amsterdam,</div>
    <div><b>Music</b> - Latin / Salsa</div>
  </div>
  <div class="manage">Manage</div>
  <div class="social">
    <span></span><span></span><span></span>
    <svg width="22" height="18" viewBox="0 0 22 18"><rect x="1" y="2" width="20" height="14" rx="1" fill="#9c9c9c"/><path d="M1 3l10 7 10-7" stroke="#1d1d1d" stroke-width="1.6" fill="none"/></svg>
  </div>
</section>

<!-- resume -->
<section class="panel" style="top:500px;height:398px">
  <div class="rail" style="top:33px"></div>
  <div class="tab-icon" style="top:33px">
    <svg width="17" height="16" viewBox="0 0 17 16"><rect x="1" y="3" width="12" height="12" fill="none" stroke="#aaa" stroke-width="1.6"/><path d="M7 10l1-3 7-7 2 2-7 7z" fill="#aaa"/></svg>
  </div>
  <div class="tab-label" style="top:33px">Resume</div>
  <div class="resume">
    <h2>Lumen Photography</h2>
    <p>Function : Head promotions, photograper, communication, marketing, and sales.</p>
    <p>Active since : jan 2006</p>
    <p>Shoots : 500 and counting</p>
    <p>Wil jij fotograferen voor Revelmap?</p>
    <p class="body">Als je uitgaan leuk vindt, makkelijk bent in de omgang en uiteraard houdt van fotograferen, biedt Revelmap je de kans een kijkje te nemen in de wereld van de partyfotografie. Door de inzet van de fotografen is Revelmap uitgegroeid tot een van de meest toonaangevende partysites van Nederland. De betrouwbaarheid, de hoge kwaliteit van de foto's en het coveren van de belangrijkste evenementen maakt van Revelmap een van de best bezochte websites in ons vakgebied.</p>
    <h3>Belangrijk informatie</h3>
  </div>
  <div class="scroll" style="top:83px;height:280px"><i style="height:158px"></i></div>
</section>

<!-- planned events -->
<section class="panel" style="top:926px;height:420px">
  <div class="rail" style="top:33px"></div>
  <div class="tab-icon" style="top:33px">
    <svg width="16" height="16" viewBox="0 0 16 16"><rect x="1" y="2" width="14" height="13" fill="none" stroke="#aaa" stroke-width="1.5"/><rect x="1" y="2" width="14" height="3" fill="#aaa"/><path d="M4 8h2v2H4zM7 8h2v2H7zM10 8h2v2h-2zM4 11h2v2H4zM7 11h2v2H7zM10 11h2v2h-2z" fill="#aaa"/></svg>
  </div>
  <div class="tab-label" style="top:33px">Geplande evenementen</div>

  <div class="event-img" style="top:98px;background:linear-gradient(135deg,#c9eadf,#7fc8b4 50%,#eaf3ee)" role="img" aria-label="Nightshift Festival poster"><div class="date">20 augustus 2016</div></div>
  <div class="event-info" style="top:108px">
    <h4>Nightshift Festival 2016</h4>
    <ul>
      <li><svg width="14" height="12" viewBox="0 0 14 12"><path d="M7 0l7 6h-2v6H9V8H5v4H2V6H0z" fill="#aaa"/></svg>Sportpark Westerhaven, Amsterdam</li>
      <li><svg width="14" height="13" viewBox="0 0 14 13"><path d="M4 1l9-1v9.5a2 2 0 1 1-1.5-1.9V3L5.5 3.7v7.8A2 2 0 1 1 4 9.6z" fill="#aaa"/></svg>Live / Soul / Techno / Uk</li>
      <li><svg width="14" height="14" viewBox="0 0 14 14"><circle cx="7" cy="7" r="5.8" fill="none" stroke="#aaa" stroke-width="1.6"/><path d="M7 3.5V7h3" stroke="#aaa" stroke-width="1.6" fill="none"/></svg>12.00 - 23.00 uur</li>
      <li><svg width="14" height="14" viewBox="0 0 14 14"><path d="M0 0h6l8 8-6 6-8-8z" fill="#aaa"/><circle cx="3" cy="3" r="1.2" fill="#1d1d1d"/></svg>Pre-register now for NIGHTSHIFT Festival 2016 at: • http://nightshiftfestival.example/</li>
    </ul>
  </div>

  <div class="event-img" style="top:258px;background:linear-gradient(135deg,#1f7a2a,#5fbf3a 55%,#1d4f1e)" role="img" aria-label="Ritmo Plaza festival poster"><div class="date">20 1augustus 2016</div></div>
  <div class="event-info" style="top:268px">
    <h4>Recreatiegebied Meerwijde</h4>
    <ul>
      <li><svg width="14" height="12" viewBox="0 0 14 12"><path d="M7 0l7 6h-2v6H9V8H5v4H2V6H0z" fill="#aaa"/></svg>Sportpark Westerhaven, Amsterdam</li>
      <li><svg width="14" height="13" viewBox="0 0 14 13"><path d="M4 1l9-1v9.5a2 2 0 1 1-1.5-1.9V3L5.5 3.7v7.8A2 2 0 1 1 4 9.6z" fill="#aaa"/></svg>Live / Soul / Techno / Uk</li>
      <li><svg width="14" height="14" viewBox="0 0 14 14"><circle cx="7" cy="7" r="5.8" fill="none" stroke="#aaa" stroke-width="1.6"/><path d="M7 3.5V7h3" stroke="#aaa" stroke-width="1.6" fill="none"/></svg>12.00 - 23.00 uur</li>
      <li><svg width="14" height="14" viewBox="0 0 14 14"><path d="M0 0h6l8 8-6 6-8-8z" fill="#aaa"/><circle cx="3" cy="3" r="1.2" fill="#1d1d1d"/></svg>Pre-register now for NIGHTSHIFT Festival 2016 at: • http://nightshiftfestival.example/</li>
    </ul>
  </div>
  <div class="scroll" style="top:84px;height:304px"><i style="height:162px"></i></div>
</section>

<!-- past events -->
<section class="panel" style="top:1376px;height:418px">
  <div class="rail" style="top:33px"></div>
  <div class="tab-icon" style="top:33px">
    <svg width="16" height="16" viewBox="0 0 16 16"><rect x="1" y="2" width="14" height="13" fill="none" stroke="#aaa" stroke-width="1.5"/><rect x="1" y="2" width="14" height="3" fill="#aaa"/><rect x="4" y="0" width="2" height="4" fill="#aaa"/><rect x="10" y="0" width="2" height="4" fill="#aaa"/></svg>
  </div>
  <div class="tab-label" style="top:33px">Past events</div>

  <div class="event-img" style="top:98px;background:linear-gradient(135deg,#f4f1ea,#ffffff 50%,#e8e2f0)" role="img" aria-label="Outdoor dance event poster with pastel stripes"><div class="date">20 augustus 2016</div></div>
  <div class="event-info" style="top:108px">
    <h4>Nightshift Festival 2016</h4>
    <ul>
      <li><svg width="14" height="12" viewBox="0 0 14 12"><path d="M7 0l7 6h-2v6H9V8H5v4H2V6H0z" fill="#aaa"/></svg>Sportpark Westerhaven, Amsterdam</li>
      <li><svg width="14" height="13" viewBox="0 0 14 13"><path d="M4 1l9-1v9.5a2 2 0 1 1-1.5-1.9V3L5.5 3.7v7.8A2 2 0 1 1 4 9.6z" fill="#aaa"/></svg>Live / Soul / Techno / Uk</li>
      <li><svg width="14" height="14" viewBox="0 0 14 14"><circle cx="7" cy="7" r="5.8" fill="none" stroke="#aaa" stroke-width="1.6"/><path d="M7 3.5V7h3" stroke="#aaa" stroke-width="1.6" fill="none"/></svg>12.00 - 23.00 uur</li>
      <li><svg width="14" height="14" viewBox="0 0 14 14"><path d="M0 0h6l8 8-6 6-8-8z" fill="#aaa"/><circle cx="3" cy="3" r="1.2" fill="#1d1d1d"/></svg>Pre-register now for NIGHTSHIFT Festival 2016 at: • http://nightshiftfestival.example/</li>
    </ul>
  </div>

  <div class="event-img" style="top:258px;background:#1e3246" role="img" aria-label="Dark blue event poster"><div class="date">20 1augustus 2016</div></div>
  <div class="event-info" style="top:268px">
    <h4>Recreatiegebied Meerwijde</h4>
    <ul>
      <li><svg width="14" height="12" viewBox="0 0 14 12"><path d="M7 0l7 6h-2v6H9V8H5v4H2V6H0z" fill="#aaa"/></svg>Sportpark Westerhaven, Amsterdam</li>
      <li><svg width="14" height="13" viewBox="0 0 14 13"><path d="M4 1l9-1v9.5a2 2 0 1 1-1.5-1.9V3L5.5 3.7v7.8A2 2 0 1 1 4 9.6z" fill="#aaa"/></svg>Live / Soul / Techno / Uk</li>
      <li><svg width="14" height="14" viewBox="0 0 14 14"><circle cx="7" cy="7" r="5.8" fill="none" stroke="#aaa" stroke-width="1.6"/><path d="M7 3.5V7h3" stroke="#aaa" stroke-width="1.6" fill="none"/></svg>12.00 - 23.00 uur</li>
      <li><svg width="14" height="14" viewBox="0 0 14 14"><path d="M0 0h6l8 8-6 6-8-8z" fill="#aaa"/><circle cx="3" cy="3" r="1.2" fill="#1d1d1d"/></svg>Pre-register now for NIGHTSHIFT Festival 2016 at: • http://nightshiftfestival.example/</li>
    </ul>
  </div>
  <div class="scroll" style="top:86px;height:302px"><i style="height:162px"></i></div>
</section>

<!-- photos -->
<section class="panel" style="top:1833px;height:418px">
  <div class="rail" style="top:35px"></div>
  <div class="tab-icon" style="top:35px">
    <svg width="17" height="15" viewBox="0 0 17 15"><rect x="1" y="1" width="15" height="13" fill="none" stroke="#aaa" stroke-width="1.5"/><path d="M3 12l4-5 3 3 2-2 3 4z" fill="#aaa"/><circle cx="5" cy="5" r="1.4" fill="#aaa"/></svg>
  </div>
  <div class="tab-label" style="top:35px">Foto's</div>

  <div class="photo" style="left:69px;top:100px;width:291px;height:291px;background:linear-gradient(160deg,#f2f2f2 0%,#d9c3a0 40%,#e07a1f 75%,#5a3a22)" role="img" aria-label="Party photo of Gordon in an orange suit and white hat"></div>
  <div class="photo" style="left:374px;top:100px;width:137px;height:138px;background:linear-gradient(160deg,#f4a640,#e06a14 55%,#3a2418)" role="img" aria-label="Party photo in orange outfits"></div>
  <div class="photo" style="left:524px;top:100px;width:137px;height:138px;background:linear-gradient(170deg,#b9c7d8,#a8855e 50%,#e2701c)" role="img" aria-label="Street party photo"></div>
  <div class="photo" style="left:675px;top:100px;width:137px;height:138px;background:linear-gradient(170deg,#9eb27a,#5a4032 50%,#e26f1a)" role="img" aria-label="Party photo with friends"></div>
  <div class="photo" style="left:825px;top:100px;width:140px;height:138px;background:linear-gradient(170deg,#f0ece4,#c59a70 50%,#e4721d)" role="img" aria-label="Party photo in white hat"></div>
  <div class="photo" style="left:374px;top:252px;width:137px;height:138px;background:linear-gradient(170deg,#9a6b4a,#d8661a 55%,#2c2420)" role="img" aria-label="Street party photo in orange suit"></div>
  <div class="photo" style="left:524px;top:252px;width:137px;height:138px;background:linear-gradient(170deg,#4a3428,#8a5a3c 50%,#1a1412)" role="img" aria-label="Indoor party photo of two friends"></div>
  <div class="photo" style="left:675px;top:252px;width:137px;height:138px;background:linear-gradient(170deg,#c7b9a6,#8a6a52 45%,#e2701c)" role="img" aria-label="Party photo on the street"></div>
  <div class="photo" style="left:825px;top:252px;width:140px;height:138px;background:linear-gradient(170deg,#a8c48c,#7a5038 50%,#e06a1a)" role="img" aria-label="Party photo with a friend"></div>
  <div class="scroll" style="top:86px;height:302px"><i style="height:162px"></i></div>
</section>

<footer class="footer">
  <div class="footer-links"><span>CONTACT</span>|<span>GEBRUIKERSVOORWAARDEN</span>|<span>PRIVACY POLICY</span></div>
  <div class="copyright">© 2004 - 2016 Revelmap</div>
</footer>

</body>
</html>
```